Financial Advisor Business Card

This business card is mainly a card for me personally (Marcus Tellavino) providing services as a Financial Planner and Accountant. My title is: Worth.while Mentor
Details provided about Harbourline Wealth Partners on the reverse side of the card is not dominant information, it is provided for ease of contact/communication purposes for prospective clients.
About me: I provide financial advice to my clients however due to regulatory issues in my industry I cannot use the title "Financial Advisor".
Target market is 25 y/o and onwards projecting a cutting edge, innovative and modern marketing influence.
Target Market(s)
25 years old and older
Industry/Entity Type
Financial
Contact Information for Business Card
Front side of business card
Name: Marcus Tellavino
Position: Worth.while Mentor
Accreditations:
Dip FS(FP)
B.Comm
Mobile: 0438 729 507
e-mail: mt@harbourwp.com.au
website: www.harbourwp.com.au
Reverse side of business card
Name: Marcus Tellavino
Company: Harbourline Wealth Partners
Position: Senior Accountant
Address:
Level 6, Suite 4
47 Gullwing Street
PO Box 872
WESTHAVEN NSW 2618
Phone: (02) 49175381
Requirements
Must have
- - Cutting edge, innovative, fun but professional, modern marketing design and fonts
- Professional and legible
- Futuristic sharp lines, some with rounded edges
- Preferred Front Card colour scheme: Black background, Silver Text, White Text, Red & Silver lines
- Preferred Reverse Card colour scheme: White background, Silver Text, Black Text, Aqua & Silver lines
Nice to have
- Design a cutting edge logo of my intials as capital letters: MT
with a bigger D and smaller K - Preferred colour is Silver Text
Should not have
- Must not be:
- vintage/classic
- stereotypical accountant/tax agent/money style business card
- old style fonts e.g. times new roman

```html
<!DOCTYPE html>
<html lang="en">
<head>
<meta charset="utf-8">
<title>Marcus Tellavino – Business Card</title>
<link rel="stylesheet" href="https://fonts.googleapis.com/css2?family=Barlow:wght@400;500;600&display=swap">
<style>
  :root {
    --bg: #ececec;
    --card-white: #f7f7f7;
    --lime: #9ccb3b;
    --blue: #3a55a4;
    --ink: #2f3033;
    --white: #ffffff;
    --rule: #8a8c90;
  }
  * { box-sizing: border-box; margin: 0; padding: 0; }
  html, body {
    width: 1200px; height: 1000px; overflow: hidden;
    background: var(--bg);
    font-family: "Barlow", "Helvetica Neue", Arial, sans-serif;
  }
  .canvas { position: relative; width: 1200px; height: 1000px; }

  .card {
    position: absolute;
    width: 560px; height: 320px;
    left: 320px;
    box-shadow: 0 10px 28px rgba(0,0,0,0.12), 0 2px 6px rgba(0,0,0,0.08);
  }

  /* Front */
  .card--front { top: 110px; background: var(--lime); }
  .front-block {
    position: absolute; right: 52px; top: 96px;
    text-align: right;
  }
  .front-name {
    font-size: 58px; font-weight: 500; line-height: 1;
    letter-spacing: 0.5px; color: var(--blue);
  }
  .front-title, .front-accred {
    font-size: 14px; color: var(--white); letter-spacing: 0.3px; line-height: 1.35;
  }
  .front-title { margin-top: 10px; }
  .front-contact {
    margin-top: 16px; font-size: 18px; color: var(--white); letter-spacing: 0.6px;
  }
  .front-contact .sep { margin: 0 8px; }
  .front-web {
    font-size: 18px; font-weight: 600; color: var(--blue); letter-spacing: 0.6px; margin-top: 2px;
  }

  /* Back */
  .card--back { top: 570px; background: var(--card-white); }
  .wordmark {
    position: absolute; right: 40px; top: 34px; text-align: left;
  }
  .wordmark-name {
    font-size: 40px; font-weight: 500; line-height: 0.9; color: var(--blue);
  }
  .wordmark-tagline {
    font-size: 14px; font-weight: 500; color: var(--ink); margin-top: 4px;
  }
  .accent-bar {
    position: absolute; left: 0; top: 206px; width: 16px; height: 40px;
  }
  .company-block {
    position: absolute; left: 32px; top: 204px; color: var(--ink);
    font-size: 13px; line-height: 1.3;
  }
  .company-name { font-weight: 600; font-size: 14px; }
  .company-address { margin-top: 10px; }
  .contact-block {
    position: absolute; left: 318px; top: 204px;
    padding-left: 12px; border-left: 1px solid var(--rule);
    color: var(--ink); font-size: 13px; line-height: 1.3;
  }
</style>
</head>
<body>
<main class="canvas">

  <section class="card card--front" aria-label="Card front">
    <div class="front-block">
      <h1 class="front-name">marcustellavino</h1>
      <p class="front-title">Worth.while Mentor</p>
      <p class="front-accred">Accreditations: Dip FS(FP) B.Comm</p>
      <p class="front-contact">0438 729 507<span class="sep">|</span>mt@harbourwp.com.au</p>
      <p class="front-web">www.harbourwp.com.au</p>
    </div>
  </section>

  <section class="card card--back" aria-label="Card back">
    <div class="wordmark">
      <p class="wordmark-name">marcus<br>tellavino</p>
      <p class="wordmark-tagline">Worth.while Mentor</p>
    </div>

    <svg class="accent-bar" viewBox="0 0 16 40" aria-hidden="true">
      <rect x="0" y="0" width="16" height="20" fill="var(--blue)"/>
      <rect x="0" y="20" width="16" height="20" fill="var(--lime)"/>
    </svg>

    <div class="company-block">
      <p class="company-name">Harbourline Wealth Partners</p>
      <p class="company-role">Senior Accountant</p>
      <p class="company-address">Level 6, Suite 4 47 Gullwing Street<br>PO Box 872 WESTHAVEN<br>NSW 2618</p>
    </div>

    <div class="contact-block">
      <p>(02) 49175381</p>
      <p>mt@harbourwp.com.au</p>
      <p>www.harbourwp.com.au</p>
    </div>
  </section>

</main>
</body>
</html>
```